In house, web site post, social media post, and email blast specials/promo flyer

We are looking to update our monthly specials flyer to be sent out via Constant Contacts as well as printed and handed out in office and social media and posted to our website. Please see attachments below for a sample of a previous flyer. We want it to look clean and not too busy. It should be professional looking as this is going to a higher end client that is paying cash for our services

Target Market(s)

Women and Men 35-55

Contact Information for Business Card

I am tired of our current business card and want a fresh updated look. We want something simple, clean, and modern looking.

Font styles to use
Sans Serif
Script

Colors
3377b5
34a7d8
85cae6
85abd2
cedeed
ecf7fb
eaf1f7

Requirements
Must have
• Clean lines, Sexy, appealing to the medical spa beauty industry. Our clients come to us to look and feel good.
• Content of actual specials:
• FIGHT FINE LINES AND WRINKLES-Purchase a minimum of 30 units of Velmox and receive a complimentary Glycolic Acid Peel ($150 VALUE)
• THE SWEAT STOPS HERE-Permanently stop underarm sweat with TessaCool treatments, starting at $1,950
• BRIGHTEN & TONE-IPL $ Laser Lumora package $3,500
• REDUCE FACE & LEG VEINS- 15% off packages
• FLORENZA: CHEEKS & NL FOLDS-SECOND SYRINGE 25% OFF, THIRD SYRINGE $50 OFF
• BODY SCULPTING FOR ABDOMEN AND THIGHS-Blast unwanted fat with a trio of treatments! $4,799
Nice to have
• Here are some sample flyers of what we would like ours to look like
• https://www.kelbrooskinspa.example/specials/
• https://marvellisaesthetics.example/november-specials-2017/

```html
<!DOCTYPE html>
<html lang="en">
<head>
<meta charset="utf-8">
<title>Solvane Monthly Specials</title>
<link rel="stylesheet" href="https://fonts.googleapis.com/css2?family=Lato:wght@400;700;900&display=swap">
<style>
  :root {
    --backdrop: #3a3a3c;
    --teal-dark: #24545c;
    --teal: #2f6d78;
    --teal-band: #3a7581;
    --heading: #3e8a90;
    --body-text: #3f8e94;
    --sky: #d5e8f5;
    --panel: #eef6fc;
    --ink: #1c1c1c;
    --white: #ffffff;
  }
  * { box-sizing: border-box; margin: 0; padding: 0; }
  html, body { width: 944px; height: 1200px; overflow: hidden; }
  body { background: var(--backdrop); font-family: "Lato", sans-serif; position: relative; }

  .flyer {
    position: absolute; left: 114px; top: 94px;
    width: 717px; height: 1013px;
    background: var(--sky); overflow: hidden;
  }
  .hero {
    position: absolute; left: 0; top: 0; width: 717px; height: 434px;
    background: linear-gradient(100deg, #a9b9b6 0%, #c7d2d0 30%, #b58a64 55%, #d9bf98 68%, #7b8a86 85%, #4f5e55 100%);
  }
  .hero-strip {
    position: absolute; left: 0; top: 415px; width: 717px; height: 19px;
    background: var(--teal-dark); opacity: .85;
  }
  .brand {
    position: absolute; left: 0; top: 46px; width: 278px; height: 121px;
    background: linear-gradient(90deg, #ffffff 70%, rgba(255,255,255,.6) 100%);
  }
  .brand-name {
    position: absolute; left: 50px; top: 30px;
    font-size: 44px; font-weight: 400; letter-spacing: 1px; color: var(--teal);
  }
  .brand-tagline {
    position: absolute; left: 157px; top: 86px;
    font-size: 16px; font-weight: 400; color: var(--teal);
  }
  .cta-band {
    position: absolute; left: 0; top: 434px; width: 717px; height: 47px;
    background: linear-gradient(90deg, var(--teal-dark), var(--teal-band));
    color: var(--white); font-weight: 700; font-size: 16px;
    display: flex; align-items: center; justify-content: center;
    letter-spacing: .1px;
  }
  .specials {
    position: absolute; left: 22px; top: 502px; width: 672px; height: 314px;
    background: var(--panel);
  }
  .special {
    position: absolute; font-size: 15px; line-height: 18.6px; color: var(--body-text);
  }
  .special h2 {
    font-size: 15.5px; font-weight: 900; color: var(--heading); line-height: 18.6px;
  }
  .special h2.inline { display: inline; }
  .col-left { left: 36px; width: 320px; }
  .col-right { left: 383px; width: 270px; }

  .site-badge {
    position: absolute; left: 210px; top: 845px; width: 296px; height: 43px;
  }
  .site-badge svg { position: absolute; inset: 0; }
  .site-badge span {
    position: relative; display: flex; height: 100%; align-items: center; justify-content: center;
    color: var(--white); font-weight: 700; font-size: 19px;
  }
  .contact {
    position: absolute; left: 0; top: 903px; width: 717px; text-align: center;
    color: var(--ink); font-size: 13px; line-height: 17.5px;
  }
  .contact strong { font-weight: 900; font-size: 13.5px; }
  .footer-band {
    position: absolute; left: 0; top: 961px; width: 717px; height: 52px;
    background: linear-gradient(90deg, var(--teal-dark), var(--teal-band));
    color: var(--white); font-weight: 700; font-size: 12.5px;
    display: flex; align-items: center; justify-content: center;
  }
</style>
</head>
<body>
  <main class="flyer">
    <div class="hero" role="img" aria-label="Portrait photo of a woman in a woven straw hat beside a stone wall"></div>
    <div class="hero-strip"></div>

    <div class="brand">
      <div class="brand-name">SOLVANE</div>
      <div class="brand-tagline">Age Beautifully</div>
    </div>

    <div class="cta-band">PLEASE CALL TO SCHEDULE YOUR APPOINTMENT TODAY 555.014.2207</div>

    <section class="specials">
      <div class="special col-left" style="top:22px">
        <h2>FIGHT FINE LINES AND WRINKLES</h2>
        <p>Purchase a minimum of 30 units of<br>Velmox and receive a complimentary<br>Glycolic Acid Peel<br>($150 VALUE)</p>
      </div>
      <div class="special col-left" style="top:152px">
        <h2>BRIGHTEN &amp; TONE-IPL $</h2>
        <p>Laser Lumora package<br>$3,500</p>
      </div>
      <div class="special col-left" style="top:237px">
        <p><h2 class="inline">FLORENZA:</h2> CHEEKS &amp; NL FOLDS-SECOND<br>SYRINGE 25% OFF, THIRD SYRINGE<br>$50 OFF</p>
      </div>

      <div class="special col-right" style="top:22px">
        <h2>THE SWEAT STOPS HERE</h2>
        <p>Permanently stop underarm<br>sweat with TessaCool treatments,<br>starting at<br>$1,950</p>
      </div>
      <div class="special col-right" style="top:142px">
        <h2>REDUCE FACE &amp; LEG VEINS</h2>
        <p>15% off packages</p>
      </div>
      <div class="special col-right" style="top:218px; width:300px">
        <p><h2 class="inline">BODY SCULPTING FOR ABDOMEN<br>AND THIGHS</h2> Blast unwanted fat<br>with a trio of treatments!<br>$4,799</p>
      </div>
    </section>

    <div class="site-badge">
      <svg width="296" height="43" viewBox="0 0 296 43" aria-hidden="true">
        <defs>
          <linearGradient id="badgeFill" x1="0" x2="1">
            <stop offset="0" stop-color="#24545c"/>
            <stop offset="1" stop-color="#3a7581"/>
          </linearGradient>
        </defs>
        <polygon points="22,0 274,0 296,43 0,43" fill="url(#badgeFill)"/>
      </svg>
      <span>solvaneportland.example</span>
    </div>

    <div class="contact">
      <strong>SOLVANE AESTHETIC &amp; ANTI-AGING CENTER</strong><br>
      2140 NW Alder Lane, Suite 4, Portland, Oregon 97210 555.014.2207<br>
      Visit solvaneportland.example for a more beautiful body, inside and out.
    </div>

    <div class="footer-band">www.kelbrooskinspa.example/specials/ | marvellisaesthetics.example/november-specials-2017/</div>
  </main>
</body>
</html>
```